SkyvoraQ Business Cards and Stationary Design

Need a design for our business cards and stationary. I want to carry on the theme of the logo. I want the business cards to have a design on the back. I would like the business cards and the stationary to carry the same theme, design scheme, and branding

Target Market(s)

Airlines and Maintenance Facilities

Industry/Entity Type

Aviation

Contact Information for Business Card

Name
Position Title
Address: 4827 Tollbeck Lane, Harlow Point, Westmara, 34951
Office Number
Mobile Number
Email
Website

Font styles to use
Serif
Sans Serif

Colors

Designer to choose colors to be used in the design.

```html
<!DOCTYPE html>
<html lang="en">
<head>
<meta charset="utf-8">
<title>SkyvoraQ Business Card</title>
<link rel="stylesheet" href="https://fonts.googleapis.com/css2?family=Roboto+Condensed:ital,wght@0,400;0,700;1,400&display=swap">
<style>
  :root {
    --page: #e9ebee;
    --paper: #fbfbfc;
    --navy: #17356f;
    --blue-deep: #1a4690;
    --blue-mid: #1f6fb0;
    --blue-light: #2a9fd6;
    --ink-light: #ffffff;
    --ink-soft: #dbe8f5;
  }
  * { margin: 0; padding: 0; box-sizing: border-box; }
  html, body { width: 1200px; height: 960px; overflow: hidden; background: var(--page); }
  body {
    display: flex; flex-direction: column; align-items: center; justify-content: center; gap: 40px;
    font-family: "Roboto Condensed", "Arial Narrow", sans-serif;
  }
  .card {
    position: relative; width: 760px; height: 434px; overflow: hidden;
    box-shadow: 0 6px 22px rgba(20, 40, 80, 0.18);
  }

  /* Front */
  .card-front { background: var(--paper); }
  .card-front .wave { position: absolute; inset: 0; width: 100%; height: 100%; }
  .brand {
    position: absolute; left: 60px; top: 70px;
    display: flex; align-items: center; gap: 16px;
  }
  .brand-dot { width: 44px; height: 44px; border-radius: 50%; background: var(--blue-mid); }
  .brand-name {
    font-size: 40px; font-weight: 700; letter-spacing: 6px; color: var(--navy);
    text-transform: uppercase;
  }
  .website {
    position: absolute; left: 60px; bottom: 48px;
    font-size: 17px; color: var(--navy); letter-spacing: 0.5px;
  }
  .person {
    position: absolute; right: 44px; top: 64px; text-align: right; color: var(--ink-light);
  }
  .person-name { font-size: 30px; font-weight: 700; letter-spacing: 0.5px; }
  .person-title { font-size: 21px; font-style: italic; color: var(--ink-soft); margin-top: 2px; }
  .contacts {
    position: absolute; right: 44px; top: 190px; list-style: none;
    color: var(--ink-light); font-size: 17px; line-height: 1.3; text-align: right;
  }
  .contacts li { display: flex; justify-content: flex-end; align-items: center; gap: 12px; margin-bottom: 10px; }
  .contacts .lines { display: flex; flex-direction: column; }
  .contacts svg { width: 18px; height: 18px; flex: none; fill: var(--ink-light); }

  /* Back */
  .card-back {
    background: linear-gradient(160deg, var(--blue-light) 0%, var(--blue-mid) 45%, var(--navy) 100%);
    display: flex; align-items: center; justify-content: center; gap: 26px;
  }
  .back-dot { width: 70px; height: 70px; border-radius: 50%; background: #e4e6ef; }
  .back-name {
    font-size: 76px; font-weight: 700; letter-spacing: 10px; color: #e4e6ef; text-transform: uppercase;
  }
</style>
</head>
<body>

<section class="card card-front">
  <svg class="wave" viewBox="0 0 760 434" preserveAspectRatio="none" aria-hidden="true">
    <defs>
      <linearGradient id="waveFill" x1="1" y1="0" x2="0" y2="1">
        <stop offset="0" stop-color="#2a9fd6"/>
        <stop offset="0.5" stop-color="#1f6fb0"/>
        <stop offset="1" stop-color="#17356f"/>
      </linearGradient>
    </defs>
    <path d="M390,0 C500,90 470,300 330,434 L760,434 L760,0 Z" fill="url(#waveFill)"/>
  </svg>

  <div class="brand">
    <span class="brand-dot"></span>
    <span class="brand-name">SkyvoraQ</span>
  </div>
  <p class="website">www.skyvoraq.com</p>

  <div class="person">
    <p class="person-name">Marten Holloway</p>
    <p class="person-title">Chief Executive</p>
  </div>

  <ul class="contacts">
    <li>
      <span class="lines"><span>4827 Tollbeck Lane,</span><span>Harlow Point, Westmara, 34951</span></span>
      <svg viewBox="0 0 24 24"><path d="M12 2a7 7 0 0 0-7 7c0 5 7 13 7 13s7-8 7-13a7 7 0 0 0-7-7zm0 9.5A2.5 2.5 0 1 1 12 6.5a2.5 2.5 0 0 1 0 5z"/></svg>
    </li>
    <li>
      <span>+49 152 40618297</span>
      <svg viewBox="0 0 24 24"><path d="M6.6 10.8a15 15 0 0 0 6.6 6.6l2.2-2.2a1 1 0 0 1 1-.25 11.4 11.4 0 0 0 3.6.57 1 1 0 0 1 1 1V20a1 1 0 0 1-1 1A17 17 0 0 1 3 4a1 1 0 0 1 1-1h3.5a1 1 0 0 1 1 1c0 1.250.2 2.450.57 3.570a1 1 0 0 1-.25 1z"/></svg>
    </li>
    <li>
      <span>+49 152 40618297</span>
      <svg viewBox="0 0 24 24"><path d="M7 1h10a2 2 0 0 1 2 2v18a2 2 0 0 1-2 2H7a2 2 0 0 1-2-2V3a2 2 0 0 1 2-2zm0 3v14h10V4zm5 15.5a1 1 0 1 0 0 2 1 1 0 0 0 0-2z"/></svg>
    </li>
    <li>
      <span>info@skyvoraq.com</span>
      <svg viewBox="0 0 24 24"><path d="M12 2a10 10 0 1 0 5 18.7l-1-1.7A8 8 0 1 1 20 12v1.5a1.5 1.5 0 0 1-3 0V12a5 5 0 1 0-1.5 3.6A3.5 3.5 0 0 0 22 13.5V12A10 10 0 0 0 12 2zm0 13a3 3 0 1 1 0-6 3 3 0 0 1 0 6z"/></svg>
    </li>
  </ul>
</section>

<section class="card card-back">
  <span class="back-dot"></span>
  <span class="back-name">SkyvoraQ</span>
</section>

</body>
</html>
```